Broschüre KALVERIT-Fertigmischung
Zielgruppe
'KALVERIT-Fertigmischung' für die Bauwerksabdichtung (Tonabdichtung) zur Abdichtung von erdberührten Bauteilen.
Aufgabenstellung
Aus den Seiten 12-28 und 33-34 der beigefügten Information (PDF) soll eine eigene Verarbeitungsbroschüre erstellt werden, auf die in unseren Lieferscheinen mittels QR-Code verlinkt werden soll.
Format sollte DIN A4 sein. Das aktuelle Logo ist ebenfalls beigefügt.

```html
<!DOCTYPE html>
<html lang="de">
<head>
<meta charset="utf-8">
<title>KALVERIT Broschüre – Außenseite</title>
<link rel="stylesheet" href="https://fonts.googleapis.com/css2?family=Inter:wght@400;700;800&family=Roboto:wght@400;700&display=swap">
<style>
  :root {
    --blue: #1f3b9b;
    --blue-deep: #15348f;
    --green: #2e955a;
    --ink: #2b2b24;
    --white: #ffffff;
  }
  * { margin: 0; padding: 0; box-sizing: border-box; }
  html, body { width: 1200px; height: 927px; overflow: hidden; background: var(--white); }
  .sheet { position: relative; width: 1200px; height: 927px; font-family: "Inter", Arial, sans-serif; }

  /* Panel 1 */
  .panel-intro { position: absolute; left: 0; top: 0; width: 400px; height: 927px; background: var(--white); }
  .intro-band {
    position: absolute; left: 0; top: 0; width: 400px; height: 620px;
    background: linear-gradient(180deg, #ffffff 0%, #c3cddd 22%, #8ea2c7 45%, #4a67b0 72%, var(--blue-deep) 100%);
  }
  .intro-title { position: absolute; left: 53px; top: 66px; font-size: 29px; font-weight: 800; letter-spacing: -1.6px; color: var(--blue); }
  .intro-text { position: absolute; left: 53px; width: 318px; font-family: "Roboto", Arial, sans-serif; font-size: 15px; line-height: 21.6px; color: var(--white); }
  .intro-text.first { top: 154px; }
  .intro-text.second { top: 452px; }
  .intro-sub { position: absolute; left: 53px; top: 370px; font-size: 21px; line-height: 21px; font-weight: 800; letter-spacing: -1.2px; color: var(--blue); }
  .trust-claim { position: absolute; left: 53px; top: 676px; font-size: 34px; line-height: 38px; font-weight: 800; letter-spacing: -1.8px; color: var(--green); }

  /* Panel 2 */
  .panel-contact { position: absolute; left: 400px; top: 0; width: 400px; height: 927px; }
  .contact-title { position: absolute; left: 48px; top: 66px; font-size: 29px; font-weight: 800; letter-spacing: -1px; color: var(--green); }
  .contact-block { position: absolute; left: 48px; top: 154px; font-family: "Roboto", Arial, sans-serif; color: var(--ink); }
  .company { font-size: 18px; font-weight: 700; line-height: 29px; }
  .company-tag { font-size: 20px; font-weight: 700; line-height: 29px; }
  .contact-list { list-style: none; margin-top: 30px; font-size: 19px; line-height: 27.6px; }
  .contact-list li { display: flex; align-items: flex-start; gap: 6px; }
  .contact-list li.gap { margin-top: 28px; }
  .contact-list svg { flex: none; width: 20px; height: 20px; margin-top: 4px; }
  .contact-list .web { text-decoration: underline; }
  .teamwork-photo {
    position: absolute; left: 0; top: 520px; width: 400px; height: 407px;
    background: radial-gradient(ellipse at 55% 70%, #8a6a55 0%, #5a5550 35%, #3b4048 70%, #2a2e36 100%);
  }

  /* Panel 3 */
  .panel-cover { position: absolute; left: 800px; top: 0; width: 400px; height: 927px; }
  .lake-photo {
    position: absolute; inset: 0;
    background: linear-gradient(180deg, #b9c6c9 0%, #d6d5c6 22%, #c9c9b6 34%, #4f6a3e 48%, #3f5a36 54%, #9aa98f 62%, #b6b9a1 70%, #7d8d66 80%, #3f5230 100%);
  }
  .cover-name { position: absolute; left: 12px; top: 78px; font-size: 30px; font-weight: 800; letter-spacing: -0.5px; color: var(--green); }
  .slogan-shape { position: absolute; left: 0; top: 736px; width: 400px; height: 152px; }
  .slogan { position: absolute; left: 10px; top: 744px; }
  .slogan-brand { font-size: 27px; line-height: 32px; font-weight: 800; letter-spacing: -0.5px; color: var(--green); }
  .slogan-line { font-size: 31px; line-height: 34px; font-weight: 800; letter-spacing: -1.6px; }
  .slogan-line.green { color: var(--green); }
  .slogan-line.blue { color: var(--blue); }
</style>
</head>
<body>
<div class="sheet">

  <section class="panel-intro">
    <div class="intro-band"></div>
    <h2 class="intro-title">Was ist KALVERIT ?</h2>
    <p class="intro-text first">KALVERIT® ist eine speziell entwickelte Ton-Fertigmischung zur Abdichtung von Bauwerken – ganz ohne Bitumen oder Kunststoffe. Das Material verbindet jahrzehntelange Praxiserfahrung mit natürlichen Rohstoffen und eignet sich ideal für vertikale und horizontale Abdichtungen im Erdreich.</p>
    <h3 class="intro-sub">Praxisbewährt seit über<br>30 Jahren</h3>
    <p class="intro-text second">KALVERIT® wird seit 1987 in zahlreichen Projekten eingesetzt – von der Abdichtung einfacher Keller bis zur Sanierung denkmalgeschützter Bauwerke. Das Material gilt heute als Stand der Technik in der mineralischen Bauwerksabdichtung.</p>
    <p class="trust-claim">Architekten,<br>Behörden und<br>Hausbesitzer setzen<br>seit Jahrzehnten auf<br>KALVERIT®</p>
  </section>

  <section class="panel-contact">
    <h2 class="contact-title">KONTAKT</h2>
    <div class="contact-block">
      <p class="company">KALVERIT GmbH</p>
      <p class="company-tag">Bauwerksabdichtung mit Ton<br>– seit 1987</p>
      <ul class="contact-list">
        <li><svg viewBox="0 0 20 20"><circle cx="10" cy="6" r="4.5" fill="#d8263a"/><line x1="10" y1="10" x2="10" y2="19" stroke="#888" stroke-width="1.6"/></svg><span>Lindenallee 18 ·<br>30159 Hannover</span></li>
        <li class="gap"><svg viewBox="0 0 20 20"><path d="M4 2l4 1 1 4-2 2c1 2 3 4 5 5l2-2 4 1 1 4-2 2C8 18 2 12 2 4z" fill="#333"/></svg><span>Tel.: 0511 / 987 65 43</span></li>
        <li><svg viewBox="0 0 20 20"><rect x="2" y="5" width="16" height="11" fill="#eef1f5" stroke="#8a96a8"/><path d="M2 5l8 6 8-6" fill="none" stroke="#8a96a8"/></svg><span>info@kalverit-ton.de</span></li>
        <li><svg viewBox="0 0 20 20" fill="none" stroke="#3a7bc8" stroke-width="1.3"><circle cx="10" cy="10" r="8"/><ellipse cx="10" cy="10" rx="3.5" ry="8"/><line x1="2" y1="10" x2="18" y2="10"/><line x1="3.5" y1="6" x2="16.5" y2="6"/><line x1="3.5" y1="14" x2="16.5" y2="14"/></svg><span class="web">www.kalverit-ton.de</span></li>
      </ul>
    </div>
    <div class="teamwork-photo" role="img" aria-label="Foto: mehrere Hände übereinandergelegt als Zeichen der Zusammenarbeit"></div>
  </section>

  <section class="panel-cover">
    <div class="lake-photo" role="img" aria-label="Foto: ruhiger Waldsee mit Spiegelung des Abendhimmels und grünem Ufer"></div>
    <div class="cover-name">KALVERIT</div>
    <svg class="slogan-shape" viewBox="0 0 400 152" aria-hidden="true">
      <polygon points="0,133 386,149 314,0 295,0 366,136 0,136" fill="#1f3b9b"/>
      <polygon points="0,132 366,132 298,0 0,0" fill="#ffffff"/>
    </svg>
    <div class="slogan">
      <div class="slogan-brand">KALVERIT</div>
      <div class="slogan-line green">Natürlich abdichten.</div>
      <div class="slogan-line blue">Natürlich besser.</div>
    </div>
  </section>

</div>
</body>
</html>
```